Stationary for Real Estate Company
Harbor Keystone, Inc.
Project: Stationary for Real Estate Company
Industry: Real Estate
Stationary for Real Estate Company - Real Estate
Creative Brief
Use same font as used in my logo
Marcus T. Wollsteader
President & CEO
4823 Avenue K
Brooklyn, New York 11237
marcus@HarborKeystone.example
http://www.HarborKeystone.example
The logo is provided. You will notice that the logo consists of a house (with a roof and the letters H K) and separately the company name (Harbor Keystone). I would like to see stationary designs where the house is to the left of the company name; designs where the house is above the company name; and designs where the house is not too close to the company name. This is a design for stationary (i.e. business cards, letterhead, brochure, etc.). Please contact me if you have any questions.
Dear Designers, please submit only business card designs. Please do not submit complete stationary designs. As soon as a business card design has been selected by me, I will ask for you to make the same design in the other stationary. Thank you.

```html
<!DOCTYPE html>
<html lang="en">
<head>
<meta charset="utf-8">
<title>Harbor Keystone – Business Card</title>
<link rel="stylesheet" href="https://fonts.googleapis.com/css2?family=Montserrat:wght@600;700&family=Open+Sans:wght@400;600&display=swap">
<style>
  :root {
    --bg: #6f7170;
    --magenta: #c2185b;
    --magenta-light: #d8437f;
    --purple: #6a2d86;
    --orange: #f07a1f;
    --ink: #222;
    --paper: #ffffff;
  }
  * { box-sizing: border-box; margin: 0; padding: 0; }
  html, body { width: 1200px; height: 907px; overflow: hidden; }
  body {
    background: var(--bg);
    position: relative;
    font-family: "Open Sans", sans-serif;
  }
  .card {
    position: absolute;
    width: 560px;
    height: 320px;
    border-radius: 24px;
    overflow: hidden;
    box-shadow: 0 10px 24px rgba(0,0,0,.3);
  }
  /* Front */
  .card-front {
    left: 30px; top: 110px;
    background: linear-gradient(120deg, var(--magenta-light) 0%, var(--magenta) 45%, #8e3a8a 78%, var(--purple) 100%);
  }
  .front-brand {
    position: absolute;
    left: 70px; top: 128px;
    display: flex; align-items: center; gap: 16px;
  }
  .brand-dot {
    width: 34px; height: 34px; border-radius: 50%;
    background: #fff;
    flex: none;
  }
  .brand-name {
    font-family: "Montserrat", sans-serif;
    font-weight: 700;
    font-size: 28px;
    letter-spacing: 2px;
    text-transform: uppercase;
    line-height: 1.05;
  }
  .brand-name span { display: block; }
  .front-brand .brand-name { color: #fff; }

  /* Back */
  .card-back {
    left: 610px; top: 477px;
    background: var(--paper);
  }
  .card-back svg.swoosh { position: absolute; inset: 0; }
  .back-brand {
    position: absolute;
    left: 40px; top: 100px;
    display: flex; align-items: center; gap: 12px;
  }
  .back-brand .brand-dot { background: var(--magenta); width: 28px; height: 28px; }
  .back-brand .brand-name { color: var(--magenta); font-size: 21px; }
  .person {
    position: absolute; left: 40px; top: 182px;
  }
  .person-name {
    font-weight: 600; font-size: 19px; color: var(--purple);
  }
  .person-title {
    font-weight: 600; font-size: 15px; color: var(--orange); margin-top: 2px;
  }
  .divider {
    position: absolute; left: 296px; top: 90px; width: 1px; height: 150px;
    background: linear-gradient(transparent, #bbb, transparent);
  }
  .contact {
    position: absolute; left: 316px; top: 88px;
    font-size: 11.5px; color: var(--ink); line-height: 1.55;
    list-style: none;
  }
  .contact li { display: flex; align-items: center; gap: 6px; white-space: nowrap; }
  .contact .toll { color: var(--magenta); font-weight: 600; }
  .icon {
    width: 12px; height: 12px; border-radius: 50%;
    border: 1.5px solid var(--magenta);
    flex: none;
  }
</style>
</head>
<body>

  <section class="card card-front" aria-label="Business card front">
    <div class="front-brand">
      <span class="brand-dot"></span>
      <p class="brand-name"><span>Harbor</span><span>Keystone</span></p>
    </div>
  </section>

  <section class="card card-back" aria-label="Business card back">
    <svg class="swoosh" width="560" height="320" viewBox="0 0 560 320" aria-hidden="true">
      <defs>
        <linearGradient id="bandTop" x1="0" y1="0" x2="1" y2="0">
          <stop offset="0" stop-color="#c2185b"/>
          <stop offset="1" stop-color="#6a2d86"/>
        </linearGradient>
        <linearGradient id="bandBottom" x1="0" y1="0" x2="1" y2="0">
          <stop offset="0" stop-color="#6a2d86"/>
          <stop offset=".6" stop-color="#c2185b"/>
          <stop offset="1" stop-color="#d8437f"/>
        </linearGradient>
      </defs>
      <path d="M300 0 H560 V70 Q470 10 300 0 Z" fill="url(#bandTop)"/>
      <path d="M330 0 Q480 14 560 78" fill="none" stroke="#f04e23" stroke-width="4"/>
      <path d="M0 250 Q120 312 280 320 H0 Z" fill="url(#bandBottom)"/>
      <path d="M0 240 Q110 306 270 320" fill="none" stroke="#f7a21b" stroke-width="4"/>
    </svg>

    <div class="back-brand">
      <span class="brand-dot"></span>
      <p class="brand-name"><span>Harbor</span><span>Keystone</span></p>
    </div>

    <div class="person">
      <p class="person-name">Marcus T. Wollsteader</p>
      <p class="person-title">President &amp; CEO</p>
    </div>

    <div class="divider"></div>

    <ul class="contact">
      <li>4823 Avenue K</li>
      <li>Brooklyn, New York 11237</li>
      <li><span class="toll">Toll Free</span><span class="icon"></span>(800) 555-0147</li>
      <li><span class="icon"></span>(718) 555-0162</li>
      <li><span class="icon"></span>(212) 555-0183</li>
      <li><span class="icon"></span>(718) 555-0129</li>
      <li><span class="icon"></span>marcus@HarborKeystone.example</li>
      <li><span class="icon"></span>www.HarborKeystone.example</li>
    </ul>
  </section>

</body>
</html>
```